Analytics/BI tech start-up seeks sharp, creative, simple, secret agent type logo & theme

"Quarry 7 Technologies" seeks a logo design/color scheme template for NYC based tech start-up of software engineers, solutions architects, and data/BI analysts. We develop reporting solutions and analytics platforms for small-medium sized businesses. We code for database, cloud, and web/mobile apps.<br/><br/>Some *very basic, limited* sketches are attached to show ideas we've had. We need a logo and color scheme that may be used for business cards, paper letterhead and envelopes, and web pages to be published at "www.quarry7.dev".<br/><br/>We like the black/red, red/white, blue/black, white/black contrasts as a stating point, and prefer black background business cards, but open to anything if it feels like a good match. We are relying on the projects submitted here to take care of the creativity part of our image, which we work on logistics to launching our start-up. Something that could also be easily translated into black/white, grayscale would be appreciated as well. while log is important, we also need an icon that may be used as an app thumbnail. For font, we prefer all caps.<br/><br/>Business: Quarry 7 Technologies<br/>Slogan: If. Else. Us. / If -> Else -> Us / If - Else - Us / etc.<br/>Website: www.quarry.dev<br/>Icon: [Q7] , only as a starting point<br/>Theme Ideas: Sleek, futuristic, secret agent-like tech, simple, bold color contrasts, software code related<br/><br/>Feel free to reach out to jvorenko@mailbarn.example as a contact for any questions or follow up. We look forward to seeing amazing ideas!
Updates

We would like to provide the opportunity for as many different submissions as possible.

Target Market(s)

Small business owners, entrepreneurs, financial/tech companies, freelance engineers, people in need of IT assistance to elevate business

Industry/Entity Type

It Company

Contact Information for Business Card

Individual Info: Name, Position, Phone Number 1, Phone Number 2 (optional), Fax Number, email Address.
Company Info: Name, logo, icon (optional), web site, slogan

Font styles to use
Sans Serif
Other font styles liked:
• Similar to Biome Light All Caps, Hollow Meridian type style

Requirements
Must have
• Pronounced 1 in the logo, either in the word Section or not. Bold color contrast, one side with only logo or icon, possible web address too. Other side with all individual info plus logo, and/or icon and web address. If using uploaded files as a base, center the C more between the E and T, it is too closer to the T as is.
Nice to have
• Bolder font possibly, more square edged at ends of letters but still with minor curved corners. Icon suggested as a starting point is “[Q7]” and instead of a slogan, use "Data - Cloud - Web - Software" and the dividers don't necessary have to be hyphens.
Should not have
• Open to all creative ideas, try anything. Please come up with different logos than are in the attached files, they are meant as a starting point.

```html
<!DOCTYPE html>
<html lang="en">
<head>
<meta charset="utf-8">
<title>Quarry 7 Technologies – Business Card</title>
<link rel="stylesheet" href="https://fonts.googleapis.com/css2?family=Saira:wght@400;700&family=Roboto:wght@400&display=swap">
<style>
  :root {
    --backdrop: #7a4119;
    --card-dark: #000000;
    --card-light: #ffffff;
    --accent: #ff6a00;
    --ink-light: #ffffff;
    --ink-dark: #222222;
    --rule-dark: #4a4a4a;
    --rule-light: #333333;
  }
  * { box-sizing: border-box; margin: 0; padding: 0; }
  html, body { width: 1200px; height: 900px; overflow: hidden; }
  body {
    background: var(--backdrop);
    position: relative;
    font-family: "Saira", "Helvetica Neue", Arial, sans-serif;
  }
  .card { position: absolute; }
  .card__band { position: absolute; left: 0; right: 0; background: var(--accent); }

  /* Front: personal details */
  .card--front { left: 329px; top: 90px; width: 556px; height: 344px; background: var(--card-dark); }
  .card--front .card__band--top { top: 0; height: 9px; }
  .card--front .card__band--bottom { bottom: 0; height: 9px; }
  .person { position: absolute; left: 0; right: 0; top: 86px; text-align: center; }
  .person__name {
    color: var(--accent); font-weight: 700; font-size: 23px; letter-spacing: 0.5px; line-height: 26px;
  }
  .person__role { color: var(--ink-light); font-size: 17px; line-height: 22px; }
  .person__rule { width: 154px; height: 1px; background: var(--rule-dark); margin: 11px auto 20px; }
  .contact { list-style: none; color: var(--ink-light); font-size: 17px; line-height: 22.3px; }
  .contact__label { color: var(--accent); font-weight: 700; }

  /* Back: company */
  .card--back { left: 329px; top: 469px; width: 560px; height: 343px; background: var(--card-light); }
  .card--back .card__band--top { top: 0; height: 9px; }
  .card--back .card__band--bottom { bottom: 0; height: 8px; }
  .brand {
    position: absolute; left: 0; right: 0; top: 116px;
    text-align: center;
    color: var(--ink-dark); font-weight: 700; font-size: 34px;
    letter-spacing: 1px; line-height: 44px; text-transform: uppercase;
  }
  .website {
    position: absolute; left: 0; right: 0; top: 243px;
    display: flex; justify-content: center; align-items: center; gap: 6px;
    font-family: "Roboto", Arial, sans-serif; font-size: 15px; color: var(--ink-dark);
  }
  .website__rule { width: 44px; height: 1px; background: var(--rule-light); }
  .slogan {
    position: absolute; left: 0; right: 0; top: 284px;
    display: flex; justify-content: center; align-items: center; gap: 9px;
    font-family: "Roboto", Arial, sans-serif; font-size: 16px; color: var(--ink-dark); letter-spacing: 0.5px;
  }
  .slogan__dot { width: 6px; height: 6px; border-radius: 50%; background: var(--accent); }
</style>
</head>
<body>
  <section class="card card--front" aria-label="Business card front">
    <div class="card__band card__band--top"></div>
    <div class="person">
      <h1 class="person__name">MARCUS ELLERY</h1>
      <p class="person__role">Managing Director</p>
      <div class="person__rule"></div>
      <ul class="contact">
        <li><span class="contact__label">P:</span> 044-987 654 321</li>
        <li><span class="contact__label">M:</span> 044-987 654 321</li>
        <li><span class="contact__label">F:</span> 044-987 654 321</li>
        <li><span class="contact__label">E:</span> hello@quarry.dev</li>
      </ul>
    </div>
    <div class="card__band card__band--bottom"></div>
  </section>

  <section class="card card--back" aria-label="Business card back">
    <div class="card__band card__band--top"></div>
    <p class="brand">Quarry 7 Technologies</p>
    <p class="website"><span class="website__rule"></span>www.quarry.dev<span class="website__rule"></span></p>
    <p class="slogan">DATA <span class="slogan__dot"></span> CLOUD <span class="slogan__dot"></span> WEB</p>
    <div class="card__band card__band--bottom"></div>
  </section>
</body>
</html>
```